Fitness Nutrition Book to be designed

My business is an Online Fitness Training Business.
I have created a nutritional booklet that each online client will receive.
The booklet in total is 17 pages, which includes front and back cover.
Text has all been completed.
The booklet should be easy to read and using colors that convey energy, such as blues, blacks, greys, yellows, reds, etc.
I do not have photos of clients working out, but I would like to use photos that represent fitness.
Appropriate items would be Kettle Bells, Dumbbells, Battle Ropes and Slam balls
I would like the interior pages to have motivational quotes, creatively and eye catching, placed on the pages.
Quotes such as:
"If it doesn't challenge you, It wont change you!"
"Train insane or remain the same"
"Sweat is Fat Crying"
"Sore Today Strong Tomorrow"
"Motivation is what gets you started, Habit is what keeps you going"
"3 Months from now you will thank yourself"
These are all quotes that I found from googling "Motivational Fitness Quote Images."
The cover should contain our            BrovaLume logo.
with                                 "You are a part of the fitness revolution!"
Meal Plan
The only interior page that will change is the meal plan portion.
There are 5 different meal plans, 1200, 1500, 1750, 2000 & 2200 calories
I would also like the correct caloric number of the interior meal plan to be placed somewhere on the cover page as well, so that by looking at the cover page, the 1200 calorie meal plan book would be easily found and distinguishable from the 1500 calorie meal plan book.
Thank you!

Target Market(s)
Target market:
25-45 year old
60% female / 40% male
has at least one child
middle income
Gets coffee at kelmorix
States that they, "want to tone up"
Currently goes to the gym maybe 1-3 x per week
Industry/Entity Type
Business
Requirements
Must have
- Clear, easy to read and follow
- I have included a file labeled "Competitors Example" This is one of my old packets that I had made years ago. I do not like this style of cover with tons of pictures
- And the new packet I am wanting to have created should look much better.

Should not have
- This packet should not be plain and boring. There should not be any page that is simply white with small black text.

```html
<!DOCTYPE html>
<html lang="en">
<head>
<meta charset="utf-8">
<title>Nutrition Booklet – Part 2</title>
<link rel="stylesheet" href="https://fonts.googleapis.com/css2?family=Fira+Sans+Condensed:ital,wght@0,400;0,500;0,600;1,500;1,600&family=Oswald:wght@500;600&family=Open+Sans:ital,wght@0,400;0,600;1,400&display=swap">
<style>
:root{
  --board:#3b3b3b;
  --blue:#1f6fc1;
  --blue-dark:#175ba3;
  --ink:#3e3e3e;
  --grey:#55585c;
  --rule:#9aa3ad;
  --page:#ffffff;
}
*{box-sizing:border-box;margin:0;padding:0}
html,body{width:910px;height:1200px;overflow:hidden;background:var(--board)}
.board{position:relative;width:910px;height:1200px;font-family:"Open Sans",Arial,sans-serif;color:var(--ink)}
.part-tab{position:absolute;left:69px;top:0;width:124px;height:64px;background:var(--blue);color:#fff;font:400 27px/64px "Open Sans",Arial,sans-serif;text-align:center;letter-spacing:.5px}
.spread{position:absolute;left:50px;width:800px;height:518px;background:var(--page);overflow:hidden}
.spread::after{content:"";position:absolute;left:360px;top:0;width:160px;height:100%;
  background:linear-gradient(90deg,rgba(0,0,0,0) 0%,rgba(0,0,0,.04) 45%,rgba(0,0,0,.09) 56%,rgba(0,0,0,.03) 62%,rgba(0,0,0,0) 100%);pointer-events:none}
.spread.top{top:80px}
.spread.bottom{top:642px}
.abs{position:absolute}
.body{font-size:7.6px;line-height:1.28;color:var(--ink)}
.body p{margin-bottom:7.5px}
.h-blue{font-family:"Fira Sans Condensed",Arial,sans-serif;font-weight:500;color:var(--blue);line-height:1.15}
.h-lg{font-size:21.5px}
.h-md{font-size:14px}
.accent-italic{font-style:italic;color:var(--blue);font-size:9.6px;line-height:1.35}
.folio{position:absolute;bottom:0;width:10px;height:24px;background:var(--blue);color:#fff;font-size:5.5px;text-align:center;padding-top:3px}
/* plate */
.plate-title{position:absolute;left:130px;top:44px;width:240px;text-align:center;font-family:"Oswald",Arial,sans-serif;font-weight:600;color:#fff;font-size:32px;line-height:1.08;letter-spacing:1px}
.plate-title .less{display:block;color:transparent;-webkit-text-stroke:1px #2b5a8e;text-decoration:line-through;text-decoration-color:#2b5a8e;font-weight:500}
.cutlery{position:absolute;background:#4c4f53;border-radius:14px}
.photo{position:absolute;left:620px;top:0;width:180px;height:136px;background:linear-gradient(135deg,#f3f4f6 0%,#e4e8ee 45%,#c9d6ea 70%,#2d62b5 100%)}
.cols{position:absolute;display:flex;gap:12px}
.cols .body{width:170px}
/* pie legend */
.share{position:absolute;left:24px;display:flex;align-items:center;gap:8px}
.share .txt{font-size:7.6px;line-height:1.28;width:115px}
.share b{color:var(--blue);font-weight:600}
.quote-disc{position:absolute;left:176px;top:344px;width:200px;height:200px;border-radius:50%;background:var(--blue)}
.quote-text{position:absolute;left:176px;top:368px;width:200px;text-align:center;color:#fff;font-family:"Fira Sans Condensed",Arial,sans-serif;font-style:italic;font-weight:500;font-size:23px;line-height:1.08}
.quote-text strong{font-weight:600;display:block;font-size:24px}
.quote-mark{font-family:"Oswald",Arial,sans-serif;font-style:normal;font-weight:600;font-size:26px}
/* meal plan */
.plan-tab{position:absolute;left:523px;top:0;width:153px;height:40px;background:var(--blue);color:#fff;font-family:"Fira Sans Condensed",Arial,sans-serif;font-size:15px;text-align:center;line-height:46px}
.meal{position:absolute;left:419px;width:357px;border:1.5px solid var(--blue);border-left:none;background:#fff}
.meal .side{position:absolute;left:0;top:-1.5px;bottom:-1.5px;width:18px;background:var(--blue);border-radius:0 0 0 0}
.meal .side span{position:absolute;left:50%;top:50%;transform:translate(-50%,-50%) rotate(-90deg);color:#fff;font-size:7px;font-weight:600;letter-spacing:.8px;white-space:nowrap}
.meal.plain{left:435px;width:341px;border-left:1.5px solid var(--blue)}
.row{display:grid;grid-template-columns:90px 86px 22px 1fr;margin-left:22px;border-bottom:1px dashed #b9c0c8;font-size:6px;line-height:1.3;color:var(--grey);padding:4px 0 0}
.plain .row{margin-left:4px;grid-template-columns:92px 86px 22px 1fr}
.row:last-child{border-bottom:none}
.row .or{width:10px;height:10px;border-radius:50%;background:#8c939b;color:#fff;font-size:4.6px;text-align:center;line-height:10px;margin:6px auto 0}
.sub-tab{position:absolute;left:435px;height:15px;background:var(--blue);color:#fff;font-size:7px;font-weight:600;padding:3px 7px 0}
</style>
</head>
<body>
<div class="board">
  <div class="part-tab">PART 2</div>

  <!-- Spread: pages 4–5 -->
  <section class="spread top">
    <div class="cutlery" role="img" aria-label="Knife silhouette" style="left:40px;top:0;width:32px;height:168px;border-radius:0 0 30px 6px"></div>
    <div class="cutlery" role="img" aria-label="Fork silhouette" style="left:388px;top:0;width:44px;height:168px;border-radius:0 0 18px 18px"></div>
    <svg class="abs" style="left:120px;top:0" width="260" height="200" viewBox="0 0 260 200" aria-hidden="true">
      <circle cx="130" cy="88" r="128" fill="none" stroke="var(--blue)" stroke-width="2.5"/>
      <circle cx="130" cy="88" r="119" fill="var(--blue)"/>
    </svg>
    <div class="plate-title">EAT<span class="less">LESS</span>BETTER</div>

    <h2 class="abs h-blue h-lg" style="left:24px;top:208px;width:300px">Proper Nutrition Accounts for 80-90% of Your Results!</h2>
    <div class="cols" style="left:24px;top:277px">
      <div class="body">
        <p>It is absolutely necessary to combine both the fitness and nutritional components together in order to achieve your ultimate health and fitness goals.</p>
        <p>Most people would like to believe that the workout itself is the most critical component in achieving your fitness goals.</p>
        <p>Although workouts are important and it would be nearly impossible to achieve your fitness goals without them, you are only going to be in the gym a few time per week for about an hour per day, which is only 4% of your entire day.</p>
      </div>
      <div class="body">
        <p>That means that the remaining 23 hours, or 96%, of your day is spent outside of the gym, and this is the timeframe when the magic of burning body fat and building muscle is really made.</p>
        <p>While most people have the desire to lose weight, tone up, increase lean muscle mass, etc., unfortunately, they have been inundated with all sorts of information that leads to confusion and frustration, and now, they don't know what they are supposed to do at all. So they turn to fad diets, dangerous supplements, or even invasive surgeries to try and correct the problem only to be let down by little to no real substantial results.</p>
      </div>
    </div>
    <div class="folio" style="left:24px">4</div>

    <div class="photo" role="img" aria-label="Photo of a pair of blue 2 kg dumbbells on a white surface"></div>
    <h3 class="abs h-blue h-md" style="left:424px;top:147px">We Create Road Maps!</h3>
    <div class="cols" style="left:424px;top:165px">
      <div class="body">
        <p>This is one of my favorite analogies, and I've used it for years. I tell people that all I do is create road maps.</p>
        <p>For example:<br>I can draw you a map to get you from San Diego, California to San Francisco, California, and as long as you follow the map that I've created, I can guarantee that you'll get to San Francisco the quickest way possible.</p>
      </div>
      <div class="body">
        <p>But if you start turning down random side streets in central California, you may get lost and never make it to San Francisco.</p>
        <p style="margin-bottom:2px">It's the same with fitness. I am simply drawing you a road map to get you from where you are now to where you want to be, and as long as you follow this road map,</p>
        <p class="accent-italic">You will get to your destination.</p>
      </div>
    </div>
    <h3 class="abs h-blue h-md" style="left:424px;top:287px">We Don't Count Calories!</h3>
    <div class="cols" style="left:424px;top:305px">
      <div class="body">
        <p>We are here to get you the results that you desire, but we are also here to educate in the process. The first rule of your meal plan is that we never count calories!</p>
        <p>Calories are not all created equally, and it's important to know where our calories are coming from.</p>
        <p>We know that in order to burn just one pound of body fat, we have to incinerate 3,500 calories. And in order to burn those calories, we have to give your body a reason to burn them, which means that we have to create a slight caloric deficit.</p>
      </div>
      <div class="body">
        <p>So, it's important that we come up with a caloric baseline that will create a slight calorie deficit, but here's where things get technical.</p>
        <p>It's not the calories that are so important.<br>It's the ratios of how your calories are divided up that is important!</p>
        <p>All calories are not created equally, so what we have to do is dedicate certain percentages of calories to three main components that fuel our metabolisms.</p>
        <p>Those three components are proteins, carbohydrates, and fats.</p>
      </div>
    </div>
    <div class="folio" style="left:766px">5</div>
  </section>

  <!-- Spread: pages 6–7 -->
  <section class="spread bottom">
    <div class="body abs" style="left:24px;top:66px;width:170px">
      <p>Your meal plan, which you will find momentarily, has been created on the 40-40-20 principle.</p>
      <p>What this means is that we took your total caloric intake and divided it up amongst proteins, carbohydrates, and fats in order to get a desired result.</p>
    </div>
    <div class="share" style="top:142px">
      <svg width="44" height="44" viewBox="-22 -22 44 44" aria-hidden="true"><circle r="21" fill="#4f5357"/><path d="M0 0 L0 -21 A21 21 0 0 1 12.3 17 Z" fill="var(--blue)" stroke="#fff" stroke-width="1"/><path d="M0 0 L-20 6.5" stroke="#fff" stroke-width="1"/></svg>
      <div class="txt"><b>Forty percent</b> of your daily calories have been dedicated to protein.</div>
    </div>
    <div class="share" style="top:201px">
      <svg width="44" height="44" viewBox="-22 -22 44 44" aria-hidden="true"><circle r="21" fill="#4f5357"/><path d="M0 0 L-20 6.5 A21 21 0 0 0 12.3 17 Z" fill="var(--blue)" stroke="#fff" stroke-width="1"/><path d="M0 0 L0 -21" stroke="#fff" stroke-width="1"/></svg>
      <div class="txt"><b>Forty percent</b> of your daily calories have been dedicated to carbohydrates.</div>
    </div>
    <div class="share" style="top:259px">
      <svg width="44" height="44" viewBox="-22 -22 44 44" aria-hidden="true"><circle r="21" fill="#4f5357"/><path d="M0 0 L0 -21 A21 21 0 0 1 20 -6.5 Z" fill="var(--blue)" stroke="#fff" stroke-width="1"/><path d="M0 0 L-12.3 17 M0 0 L20 -6.5" stroke="#fff" stroke-width="1"/></svg>
      <div class="txt"><b>Twenty percent</b> of your daily calories have been dedicated to fats.</div>
    </div>
    <div class="body abs" style="left:24px;top:327px;width:170px">
      <p>What this ratio does is allow your body to become a fat-burning machine while also allowing you to sustain and build lean muscle mass as well as fueling your metabolism so that you have a surplus of consistent energy.</p>
    </div>

    <h3 class="abs h-blue h-md" style="left:204px;top:68px;width:150px">We've Done All the Math for You!</h3>
    <div class="body abs" style="left:204px;top:104px;width:172px">
      <p>Soon, you will find your meal plan.</p>
      <p>And we have already done all of the math for you! Your meal plan contains the correct caloric intake, correct ratios, and correct portion sizes for every single meal.</p>
      <p>Your body will have no choice but to change! Now, this meal plan isn't the typical one-page meal plan that has you eating chicken and broccoli every day for the rest of your life. That is not realistic!</p>
      <p>We created a meal plan that is extremely simple to follow and is loaded with tons of options so that you'll never get bored.</p>
      <p class="accent-italic">Without further ado,<br>I present your meal plan...</p>
    </div>
    <svg class="abs" style="left:324px;top:276px" width="10" height="16" viewBox="0 0 10 16" aria-hidden="true"><path d="M0 0 L10 8 L0 16 Z" fill="var(--blue)"/></svg>

    <div class="quote-disc"></div>
    <div class="quote-text"><span class="quote-mark">“</span> SORE TODAY<strong>STRONG</strong><strong>TOMORROW <span class="quote-mark">”</span></strong></div>
    <div class="folio" style="left:24px">6</div>

    <!-- Meal plan -->
    <div class="plan-tab">1250 Calories Meal Plan</div>

    <div class="meal" style="top:50px;height:109px">
      <div class="side"><span>BREAKFAST</span></div>
      <div class="row" style="height:36px"><div>Protein<br>17 grams</div><div>1 whole egg &amp;<br>3 egg whites</div><div class="or">Or</div><div>1 scoop protein powder<br>6 ounces nonfat Greek yogurt<br>5 ounces low fat cottage cheese</div></div>
      <div class="row" style="height:36px"><div>Carbohydrate<br>13 grams</div><div>2 ounces black beans</div><div class="or">Or</div><div>1 slice Vitagrain bread<br>¼ cup oats (uncooked)<br>2 plain rice cakes</div></div>
      <div class="row" style="height:34px"><div>Fat 8 grams</div><div>1/3 avocado</div><div class="or">Or</div><div>1 TBS almond butter<br>2 TBS chia seeds<br>12 almonds</div></div>
    </div>

    <div class="meal" style="top:164px;height:110px">
      <div class="side"><span>LUNCH</span></div>
      <div class="row" style="height:36px;grid-template-columns:78px 98px 22px 1fr"><div>Protein<br>21 grams</div><div>3 ounces chicken breast</div><div class="or">Or</div><div>3 ounces canned tuna in water<br>4 ounces lean ground turkey (97% lean)<br>3 ounces sliced turkey breast</div></div>
      <div class="row" style="height:36px;grid-template-columns:78px 98px 22px 1fr"><div>Carbohydrate<br>14 grams</div><div>3 ounces black beans</div><div class="or">Or</div><div>¼ cup brown rice (cooked)<br>2 ounces yam<br>2 rice cake</div></div>
      <div class="row" style="height:19px;grid-template-columns:78px 98px 22px 1fr"><div>Fats</div><div style="grid-column:2/5">1 TBS balsamic vinaigrette</div></div>
      <div class="row" style="height:17px;grid-template-columns:78px 98px 22px 1fr"><div>Veggies</div><div>1 large salad</div><div></div><div>At least 5 vegetables. As much as you can eat.</div></div>
    </div>

    <div class="sub-tab" style="top:279px;width:75px">PM SNACK</div>
    <div class="meal plain" style="top:294px;height:27px">
      <div class="row" style="height:24px;grid-template-columns:74px 98px 22px 1fr"><div>Fat<br>14 grams</div><div>22 almonds</div><div class="or" style="margin-top:3px">Or</div><div>½ avocado<br>2 TBS almond butter</div></div>
    </div>

    <div class="meal" style="top:325px;height:76px">
      <div class="side"><span>DINNER</span></div>
      <div class="row" style="height:36px;grid-template-columns:78px 98px 22px 1fr"><div>Protein<br>26 grams</div><div>4 ounces chicken breast</div><div class="or">Or</div><div>4 ounces salmon<br>4 ounces lean ground turkey (97% lean)<br>4 ounces Tri-Tip steak</div></div>
      <div class="row" style="height:19px;grid-template-columns:78px 98px 22px 1fr"><div>Fats</div><div style="grid-column:2/5">1 TBS balsamic vinaigrette</div></div>
      <div class="row" style="height:18px;grid-template-columns:78px 98px 22px 1fr"><div>Veggies</div><div>1 large salad</div><div></div><div>At least 5 vegetables. As much as you can eat.</div></div>
    </div>

    <div class="sub-tab" style="top:406px;width:123px">POST WORKOUT SHAKE</div>
    <div class="meal plain" style="top:421px;height:28px">
      <div class="row" style="height:25px;grid-template-columns:74px 120px 1fr"><div>Protein<br>24-30 grams</div><div>1 scoop protein powder</div><div>Drink immediately after workout</div></div>
    </div>
    <div class="folio" style="left:766px">7</div>
  </section>
</div>
</body>
</html>
```